Sunfable Preschool UI Design

**This has to be designed in landscape and NOT portrait :)
We need a user interface design for login screen we will have displayed at all times on our iPads in the reception area. These iPads will log our "Tinkerlings" in and out using a login and password, and will sign them in for the day. This is a brand new, state-of-the-art 21st century learning environment. Our logo was made my a designer on pixelbazaar :)
We will have 2 main login screens:
one for admin
one for parents
I would like something fun and playful - and possibly "natural" looking as we are a Reggio Emilia inspired program (similar to Montessori).
Please visit our website to learn more about us:
www.Sunfable-example.com
I attached an example of the buttons/options we will need on the login screen - just don't think it looks great and want something more professional/sophisticated.
Thank you!
Landscape
- landscape orientation

```html
<!DOCTYPE html>
<html lang="en">
<head>
<meta charset="utf-8">
<title>Sunfable Tinkerlings – Staff Login</title>
<link rel="stylesheet" href="https://fonts.googleapis.com/css2?family=Open+Sans:wght@400;600;700&display=swap">
<style>
  :root {
    --bg-center: #f4f9f7;
    --bg-mid: #dcece8;
    --bg-edge: #b2d8d1;
    --teal: #7dbbaf;
    --stone: #616469;
    --stone-dark: #55585d;
    --mist: #cfe2dd;
    --white: #ffffff;
    --ink: #5a5d62;
  }
  * { box-sizing: border-box; margin: 0; padding: 0; }
  html, body { width: 1200px; height: 675px; overflow: hidden; }
  body { font-family: "Open Sans", Arial, sans-serif; }

  .screen {
    position: relative;
    width: 1200px;
    height: 675px;
    overflow: hidden;
    background: radial-gradient(ellipse 520px 330px at 600px 330px, var(--bg-center) 0%, var(--bg-mid) 55%, var(--bg-edge) 100%);
  }

  .nav-pill {
    position: absolute;
    top: 64px;
    width: 138px;
    height: 27px;
    border-radius: 50%;
    background: var(--white);
    border: 2px solid var(--teal);
    box-shadow: 2px 3px 5px rgba(0,0,0,0.18);
    display: flex;
    align-items: center;
    justify-content: center;
    font-size: 12px;
    font-weight: 600;
    letter-spacing: 1.5px;
    color: var(--ink);
    text-decoration: none;
  }
  .nav-home { left: 370px; }
  .nav-parents { left: 682px; }

  .brand-mark {
    position: absolute;
    left: 548px;
    top: 26px;
    width: 104px;
    height: 104px;
    border-radius: 50%;
    background: var(--white);
    border: 3px solid var(--stone);
    display: flex;
    align-items: center;
    justify-content: center;
    font-size: 17px;
    font-weight: 700;
    color: var(--stone);
  }

  .page-title {
    position: absolute;
    top: 160px;
    left: 0;
    width: 1200px;
    text-align: center;
    font-size: 58px;
    font-weight: 700;
    letter-spacing: 7px;
    color: var(--white);
    line-height: 70px;
  }

  .well-art {
    position: absolute;
    left: 366px;
    top: 278px;
    width: 436px;
    height: 397px;
    background: linear-gradient(180deg, var(--stone) 0%, var(--stone) 15%, var(--mist) 30%, var(--mist) 68%, var(--stone) 82%, var(--stone) 100%);
  }

  .roof-label {
    position: absolute;
    left: 398px;
    top: 286px;
    width: 396px;
    text-align: center;
    font-size: 28px;
    font-weight: 600;
    letter-spacing: 2px;
    line-height: 40px;
    color: var(--white);
  }

  .field {
    position: absolute;
    height: 54px;
    width: 322px;
    border-radius: 50%;
    background: var(--white);
    border: 2px solid var(--teal);
    box-shadow: 3px 4px 6px rgba(0,0,0,0.22);
    font-family: "Open Sans", Arial, sans-serif;
    font-size: 24px;
    letter-spacing: 2px;
    text-align: center;
    color: var(--ink);
    outline: none;
  }
  .field::placeholder { color: var(--ink); opacity: 1; }
  .field-username { left: 466px; top: 356px; }
  .field-password { left: 390px; top: 428px; }

  .login-button {
    position: absolute;
    left: 432px;
    top: 544px;
    width: 325px;
    height: 38px;
    border-radius: 50%;
    background: linear-gradient(#f4f8f7, #dbe9e6);
    border: 3px solid var(--stone-dark);
    box-shadow: inset 0 3px 5px rgba(0,0,0,0.15);
    font-family: "Open Sans", Arial, sans-serif;
    font-size: 20px;
    font-weight: 700;
    letter-spacing: 2px;
    color: var(--ink);
    cursor: pointer;
  }
</style>
</head>
<body>
  <main class="screen">
    <a class="nav-pill nav-home" href="#">HOME</a>
    <div class="brand-mark">Sunfable</div>
    <a class="nav-pill nav-parents" href="#">PARENTS</a>

    <h1 class="page-title">SUNFABLE TINKERLINGS</h1>

    <div class="well-art" role="img" aria-label="Illustration of a grey brick wishing well with a peaked roof and teal bubbles rising around it"></div>
    <div class="roof-label">Staff Login</div>

    <form class="login-form" action="#">
      <input class="field field-username" type="text" name="username" placeholder="username" aria-label="Username">
      <input class="field field-password" type="password" name="password" placeholder="password" aria-label="Password">
      <button class="login-button" type="submit">LOGIN</button>
    </form>
  </main>
</body>
</html>
```